【 概要 】 ナイトワーク専門のスキマバイトアプリを運営しています。事業者への訴求に特化した広告バナーを制作いただきたく思います。 【 依頼内容 】 ・サイズ: 横1080px × 縦1080px ・作成数: 1種類 ・利用用途:SNS広告など 【 デザインイメージ 】 ・ホームページデザインに似たテイスト / https://about.velto-rinka.jp ・「ナイトワーク人材足りてますか?」というテキストを強調表示 【 契約金額(税抜) 】 10,000円 / 1枚 ※契約金額(税込)からシステム利用料を差し引いた金額が、ワーカーさまの受取金額となります その他ご質問等ありましたら、気軽にお問い合わせください。 ご応募をお待ちしております。 |
どの案も素敵でしたが、この作品が最もイメージに合っていました。
この度は沢山のご応募を誠にありがとうございました。
不採用の場合でもめぼしい作品は買い取らせていただければと考えていますので、対象者には追ってご連絡させていただきます。その他、実績として制作物の掲載をご希望の方がいらっしゃいましたら、承認制にはなりますがご連絡ください。
今後ともよろしくお願いいたします。

```html
<!DOCTYPE html>
<html lang="ja">
<head>
<meta charset="UTF-8">
<title>ナイトワーク人材 足りてますか?</title>
<link href="https://fonts.googleapis.com/css2?family=Noto+Serif+JP:wght@500;700;900&family=Noto+Sans+JP:wght@700;900&display=swap" rel="stylesheet">
<style>
  :root{
    --paper:#f7f7f5;
    --ink:#141414;
    --accent-red:#e0211b;
    --navy:#1d2b4f;
    --label-blue:#34507e;
    --label-edge:#c9d3e3;
    --label-orange:#f39a2a;
    --gold-light:#d8ae5e;
    --gold-dark:#b8893d;
    --photo-dark:#15130f;
    --photo-warm:#4a3a2a;
  }
  *{margin:0;padding:0;box-sizing:border-box}
  html,body{width:1200px;height:1200px;overflow:hidden;background:var(--paper)}
  .banner{position:relative;width:1200px;height:1200px;overflow:hidden;background:var(--paper);
    font-family:"Noto Serif JP",serif;color:var(--ink)}
  .navy-wedge{position:absolute;left:0;top:0}
  .photo{position:absolute;left:430px;top:0;width:770px;height:1080px;
    background:
      radial-gradient(ellipse 260px 200px at 250px 560px, rgba(190,150,110,.55), transparent 70%),
      radial-gradient(ellipse 300px 260px at 560px 520px, rgba(150,110,80,.35), transparent 70%),
      linear-gradient(110deg, var(--photo-warm) 0%, #2a2119 30%, var(--photo-dark) 60%, #0c0b09 100%);
    clip-path:polygon(400px 0,100% 0,100% 100%,150px 100%,0 62%,0 46%,360px 31%)}
  .headline{position:absolute;left:0;top:0;width:820px;height:340px;font-weight:700}
  .headline-line{position:absolute;left:26px;display:block;white-space:nowrap;line-height:1}
  .headline-top{top:26px;font-size:78px;letter-spacing:.02em}
  .headline-bottom{top:168px;font-size:96px;letter-spacing:.01em}
  .headline-bottom .stress{color:var(--accent-red);font-size:130px;font-weight:900;vertical-align:-6px}
  .rule{position:absolute;left:0;height:4px;background:linear-gradient(90deg,var(--ink) 75%,rgba(20,20,20,0))}
  .rule-top{top:118px;width:800px}
  .rule-bottom{top:326px;width:820px}
  .tag{position:absolute;left:-30px;height:96px;display:flex;align-items:center;
    padding-left:48px;background:var(--label-blue);border:4px solid var(--label-edge);
    transform:skewX(-18deg);box-shadow:4px 6px 10px rgba(0,0,0,.25)}
  .tag span{display:block;transform:skewX(18deg);color:#fff;font-size:56px;font-weight:700;white-space:nowrap}
  .tag-pay{top:565px;width:345px}
  .tag-night{top:720px;width:575px}
  .tag-gig{top:878px;width:455px}
  .tag-gig span{color:var(--label-orange)}
  .cta{position:absolute;left:0;top:1080px;width:1200px;height:120px;
    background:linear-gradient(180deg,var(--gold-light),var(--gold-dark));
    display:flex;align-items:center;justify-content:center;gap:18px;
    font-family:"Noto Sans JP",sans-serif;font-weight:900;font-size:50px;color:var(--ink)}
  .cta svg{width:40px;height:40px}
</style>
</head>
<body>
<div class="banner">
  <svg class="navy-wedge" width="1200" height="1200" viewBox="0 0 1200 1200" aria-hidden="true">
    <polygon points="0,1080 560,670 800,670 800,1080" fill="var(--navy)"/>
  </svg>

  <div class="photo" role="img" aria-label="黒いシャツのバーテンダーがシェイカーを振る手元の写真"></div>

  <h1 class="headline">
    <span class="headline-line headline-top">ナイトワーク人材</span>
    <span class="headline-line headline-bottom"><span class="stress">足り</span>てますか?</span>
  </h1>
  <div class="rule rule-top"></div>
  <div class="rule rule-bottom"></div>

  <div class="tag tag-pay"><span>高時給!</span></div>
  <div class="tag tag-night"><span>ナイトワークの</span></div>
  <div class="tag tag-gig"><span>スキマバイト</span></div>

  <div class="cta">
    <span>登録はこちら</span>
    <svg viewBox="0 0 40 40" aria-hidden="true"><polygon points="6,4 36,20 6,36" fill="var(--ink)"/></svg>
  </div>
</div>
</body>
</html>
```